Service business needs Business Card Design

Looking to create a new business card design that is both professional and unique the can highlight the many services we offer throughout the seasons. Our tagline is "The Cobalt Advantage"
Licensed & Insured: HC731462 has to be small and on the back side of the card.
On the Front:
FirstName LastName
Title
We offer the following services:
Deck Repair and Maintenance
Deck Cleaning and Staining/Painting
Power Washing/House Washing
Landscape Lighting Installation
Christmas Lighting Installation

```html
<!DOCTYPE html>
<html lang="en">
<head>
<meta charset="utf-8">
<title>Cobalt Services – Business Card</title>
<link href="https://fonts.googleapis.com/css2?family=Montserrat:wght@400;500;600;700&display=swap" rel="stylesheet">
<style>
  :root {
    --backdrop: #3a3330;
    --card-white: #ffffff;
    --brand-deep: #0d5b9c;
    --brand-mid: #1a78bd;
    --brand-light: #3ea9dc;
    --ink: #2b2b2b;
    --ink-soft: #555555;
  }
  * { margin: 0; padding: 0; box-sizing: border-box; }
  html, body {
    width: 1200px; height: 786px; overflow: hidden;
    background: var(--backdrop);
    font-family: "Montserrat", sans-serif;
  }
  .canvas {
    width: 1200px; height: 786px;
    display: flex; align-items: center; justify-content: center; gap: 40px;
  }
  .card {
    width: 540px; height: 309px;
    position: relative;
    box-shadow: 0 10px 28px rgba(0,0,0,0.45);
  }

  /* Contact side */
  .card--contact {
    background: var(--card-white);
    display: flex; align-items: center;
    padding: 0 30px 0 34px;
  }
  .wordmark {
    display: flex; align-items: center; gap: 10px;
    color: var(--brand-deep);
  }
  .wordmark__square {
    width: 22px; height: 22px; background: var(--brand-deep);
    flex-shrink: 0;
  }
  .wordmark__text {
    font-weight: 700; line-height: 1.05;
    font-size: 30px; letter-spacing: 1px;
  }
  .wordmark__sub {
    display: block; font-size: 13px; letter-spacing: 9px;
  }
  .divider {
    width: 1.5px; height: 150px;
    background: var(--brand-mid);
    margin: 0 22px 0 26px;
    flex-shrink: 0;
  }
  .details { color: var(--ink); font-size: 12px; line-height: 1.45; }
  .details__name {
    color: var(--brand-mid); font-weight: 700; font-size: 21px; line-height: 1.1;
  }
  .details__title { font-size: 12.5px; color: var(--ink-soft); margin-bottom: 6px; }
  .details__license { font-size: 12px; margin-bottom: 8px; }
  .details__license strong { color: var(--brand-mid); font-weight: 600; }
  .contact-list { list-style: none; margin-bottom: 12px; }
  .contact-list li { display: flex; align-items: center; gap: 8px; }
  .contact-list svg { width: 11px; height: 11px; fill: var(--brand-mid); flex-shrink: 0; }
  .address { font-size: 12px; line-height: 1.35; }

  /* Services side */
  .card--services {
    background: linear-gradient(120deg, var(--brand-deep) 0%, var(--brand-mid) 55%, var(--brand-light) 100%);
    color: var(--card-white);
    display: flex; align-items: center;
    padding: 0 30px 0 36px;
    gap: 30px;
  }
  .card--services .wordmark { color: var(--card-white); }
  .card--services .wordmark__square { background: var(--card-white); }
  .services__heading { font-weight: 600; font-size: 13.5px; margin-bottom: 8px; }
  .services__list { list-style: none; font-size: 11.5px; line-height: 1.6; }
  .services__list li::before { content: "•"; margin-right: 8px; }
  .services__tagline { font-size: 11px; font-style: normal; margin-top: 10px; opacity: 0.9; letter-spacing: 0.5px; }
</style>
</head>
<body>
  <main class="canvas">
    <section class="card card--contact" aria-label="Contact side">
      <div class="wordmark">
        <span class="wordmark__square"></span>
        <span class="wordmark__text">COBALT<span class="wordmark__sub">SERVICES</span></span>
      </div>
      <div class="divider"></div>
      <div class="details">
        <p class="details__name">Daniel Rourke</p>
        <p class="details__title">CEO &amp; Founder</p>
        <p class="details__license"><strong>Licensed &amp; Insured:</strong> HC731462</p>
        <ul class="contact-list">
          <li><svg viewBox="0 0 24 24"><path d="M6.6 10.8a15.1 15.1 0 0 0 6.6 6.6l2.2-2.2a1 1 0 0 1 1-.25 11.4 11.4 0 0 0 3.6.57 1 1 0 0 1 1 1V20a1 1 0 0 1-1 1A17 17 0 0 1 3 4a1 1 0 0 1 1-1h3.5a1 1 0 0 1 1 1c0 1.25.2 2.45.57 3.57a1 1 0 0 1-.25 1z"/></svg>+1 555-014-2290</li>
          <li><svg viewBox="0 0 24 24"><path d="M2 5h20v14H2z M2 5l10 8 10-8" /></svg>info@cobaltservicesgroup.com</li>
          <li><svg viewBox="0 0 24 24"><circle cx="12" cy="12" r="10"/></svg>www.cobaltservicesgroup.com</li>
        </ul>
        <p class="address">48 Meridian Way, Suite 204<br>Harborview, PA 19000</p>
      </div>
    </section>

    <section class="card card--services" aria-label="Services side">
      <div class="wordmark">
        <span class="wordmark__square"></span>
        <span class="wordmark__text">COBALT<span class="wordmark__sub">SERVICES</span></span>
      </div>
      <div class="services">
        <p class="services__heading">We offer the following services:</p>
        <ul class="services__list">
          <li>Deck Repair and Maintenance</li>
          <li>Deck Cleaning and Staining/Painting</li>
          <li>Power Washing/House Washing</li>
          <li>Landscape Lighting Installation</li>
          <li>Christmas Lighting Installation</li>
        </ul>
      </div>
    </section>
  </main>
</body>
</html>
```